Gulf Book About Father - need cover design named - الوهج

The book talks about the good father who teaches his sons high principles and values, to be successful people in their lives.

Book size - 15 cm high
21 cm width
Data on the cover:
Name of the Book: الوهج
Author: دكتور/ وضاح بن ناصر القرملي- Just write the name without the word writer
1440-2018
Logo of the Publishing House

Target Market(s)

Book submitted to children - Families - Schools - Public libraries

Requirements
Must have
• Design must include one or all of these options:
• The first option: a picture that has a meaning for a father who has values and principles with the son or children, expresses the contradiction - education, etc. -
• The background is to express the tender love or taken from the Emirates flag
• The second option: abstract art - with a background taken from the colors of the flag of the Emirates - or colors about love and tenderness
Should not have
• direct image

```html
<!DOCTYPE html>
<html lang="ar" dir="rtl">
<head>
<meta charset="utf-8">
<title>الوهج — غلاف الكتاب</title>
<link rel="stylesheet" href="https://fonts.googleapis.com/css2?family=Lalezar&family=Tajawal:wght@500;700&display=swap">
<style>
  :root {
    --page-bg: #f2e9dc;
    --cover-top: #6a2a8c;
    --cover-mid: #4a2e92;
    --cover-bottom: #5a2a8a;
    --band: rgba(170, 60, 170, 0.35);
    --band-soft: rgba(150, 70, 190, 0.22);
    --title-yellow: #ffe04a;
    --title-edge: #f08a1c;
    --text-yellow: #f7d64a;
    --art-warm: #fff1a8;
    --art-pink: #e95bb3;
    --art-red: #ff3d5e;
    --ring: #3a1f78;
  }
  * { margin: 0; padding: 0; box-sizing: border-box; }
  html, body { width: 1200px; height: 893px; overflow: hidden; background: var(--page-bg); }
  .book-cover {
    position: absolute; left: 40px; top: 46px; width: 1120px; height: 800px;
    background: linear-gradient(160deg, var(--cover-top) 0%, var(--cover-mid) 45%, var(--cover-bottom) 100%);
    overflow: hidden;
  }
  .band { position: absolute; left: 0; right: 0; }
  .band--top { top: 22px; height: 34px; background: var(--band); }
  .band--top-soft { top: 120px; height: 48px; background: var(--band-soft); }
  .band--bottom { top: 560px; height: 60px; background: var(--band-soft); }
  .spine-hinge { position: absolute; top: 0; bottom: 0; left: 26px; width: 2px; background: rgba(30, 10, 60, 0.35); }
  .cover-art {
    position: absolute; left: 440px; top: 150px; width: 390px; height: 390px; border-radius: 50%;
    background: linear-gradient(180deg, var(--art-warm) 0%, #ffd86a 45%, var(--art-pink) 72%, var(--art-red) 100%);
    box-shadow: 0 0 0 8px var(--ring);
  }
  .book-title {
    position: absolute; left: 560px; top: 360px; width: 320px; text-align: center;
    font-family: "Lalezar", sans-serif; font-size: 170px; line-height: 1;
    color: var(--title-yellow);
    -webkit-text-stroke: 3px var(--title-edge);
    text-shadow: 0 0 14px rgba(255, 220, 80, 0.7);
  }
  .author {
    position: absolute; left: 490px; top: 560px; width: 460px; text-align: center;
    font-family: "Tajawal", sans-serif; font-weight: 700; font-size: 30px; color: var(--text-yellow);
  }
  .date {
    position: absolute; left: 490px; top: 604px; width: 460px; text-align: center;
    font-family: "Tajawal", sans-serif; font-weight: 700; font-size: 30px; color: var(--text-yellow);
  }
  .publisher {
    position: absolute; right: 44px; top: 320px; width: 70px; height: 62px;
    background: #fff; display: flex; flex-direction: column; align-items: center; justify-content: center; gap: 4px;
  }
  .publisher-mark { width: 22px; height: 22px; background: #7a3b1e; }
  .publisher-name { font-family: "Tajawal", sans-serif; font-weight: 700; font-size: 11px; color: #7a3b1e; }
</style>
</head>
<body>
  <main class="book-cover">
    <div class="band band--top"></div>
    <div class="band band--top-soft"></div>
    <div class="band band--bottom"></div>
    <div class="spine-hinge"></div>
    <div class="cover-art" role="img" aria-label="صورة أب يمسك بيد ابنه على كثبان رملية بألوان دافئة"></div>
    <h1 class="book-title">الوهج</h1>
    <p class="author">دكتور / وضاح بن ناصر القرملي</p>
    <p class="date">١٤٤٠-٢٠١٨</p>
    <div class="publisher">
      <span class="publisher-mark"></span>
      <span class="publisher-name">دار النخلة</span>
    </div>
  </main>
</body>
</html>
```